Tulmex Business Card

I already have the conplay logo. I need to develop a professional business card layout

Target Market(s)

Business

Industry/Entity Type

Business

Contact Information for Business Card

Company Name: Tulmex Limited

Font styles to use
Sans Serif

Colors

Designer to choose colors to be used in the design.

Requirements
Must have
• Use current logo
• Need two card size options:
• Small Card: 70mm x 28mm (Landscape)
• Square Card: 65mm x 65mm
Nice to have
• I will need 8-10 files for each name, number and email address (details to follow)

```html
<!DOCTYPE html>
<html lang="en">
<head>
<meta charset="utf-8">
<title>Tulmex Business Card</title>
<link rel="stylesheet" href="https://fonts.googleapis.com/css2?family=Poppins:wght@400;600;700&display=swap">
<style>
  :root {
    --backdrop: #3a3733;
    --card-dark: #221f1f;
    --card-light: #ffffff;
    --accent-blue: #29a8e0;
    --accent-yellow: #f4d20c;
    --text-light: #f2f2f2;
  }
  * { margin: 0; padding: 0; box-sizing: border-box; }
  html, body {
    width: 1200px; height: 930px; overflow: hidden;
    background: var(--backdrop);
    font-family: "Poppins", sans-serif;
  }
  .canvas { position: relative; width: 1200px; height: 930px; }

  /* Scale: 8px per mm */
  .card {
    position: absolute;
    border-radius: 14px;
    overflow: hidden;
    background: var(--card-dark);
    box-shadow: 0 10px 28px rgba(0,0,0,0.35);
  }
  /* Square card 65 x 65 mm */
  .card--square { left: 60px; top: 60px; width: 520px; height: 520px; }
  /* Small card 70 x 28 mm */
  .card--small { left: 600px; top: 640px; width: 560px; height: 224px; }

  .wordmark {
    font-family: "Poppins", sans-serif;
    font-weight: 700;
    color: var(--accent-blue);
    letter-spacing: 2px;
    line-height: 1;
    white-space: nowrap;
  }
  .card--square .wordmark {
    position: absolute; left: 0; right: 0; top: 50%;
    transform: translateY(-50%);
    text-align: center;
    font-size: 80px;
  }

  .front-panel { position: absolute; inset: 0; }
  .card--small .wordmark {
    position: absolute; left: 275px; top: 34px;
    font-size: 46px;
  }

  .contact {
    position: absolute; left: 24px; top: 90px;
    color: var(--text-light);
    font-size: 11.5px; line-height: 15px;
  }
  .contact__name {
    color: var(--accent-yellow);
    font-weight: 600; font-size: 19px; line-height: 23px;
    text-transform: uppercase;
    white-space: nowrap;
  }
  .contact__address { margin-bottom: 3px; }
  .contact__row { display: flex; align-items: center; gap: 7px; }
  .contact__icon { width: 10px; height: 10px; flex: none; }
</style>
</head>
<body>
<div class="canvas">

  <section class="card card--square" aria-label="Square card, 65 by 65 mm">
    <div class="wordmark">TULMEX</div>
  </section>

  <section class="card card--small" aria-label="Small card, 70 by 28 mm">
    <svg class="front-panel" width="560" height="224" viewBox="0 0 560 224">
      <path d="M136,0 Q226,172 560,148" fill="none" stroke="var(--accent-blue)" stroke-width="4"/>
      <path d="M150,0 Q240,160 560,140 L560,0 Z" fill="var(--card-light)"/>
    </svg>
    <div class="wordmark">TULMEX</div>

    <div class="contact">
      <p class="contact__name">Daniel Harper</p>
      <p class="contact__role">Director</p>
      <p class="contact__address">752 Maple Ridge Rd.<br>Franklin, TN 37064</p>
      <p class="contact__row">
        <svg class="contact__icon" viewBox="0 0 12 12"><path d="M2.5 1 L4.5 1 L5.2 3.6 L4 4.6 Q5 7 7.4 8 L8.4 6.8 L11 7.5 L11 9.5 Q10 11 8 10.6 Q2.5 9 1.2 3.6 Q1 1.8 2.5 1 Z" fill="var(--accent-yellow)"/></svg>
        +1-555-014-2087
      </p>
      <p class="contact__row">
        <svg class="contact__icon" viewBox="0 0 12 12"><rect x="1" y="2.5" width="10" height="7" fill="none" stroke="var(--accent-yellow)" stroke-width="1.3"/><path d="M1 2.5 L6 6.5 L11 2.5" fill="none" stroke="var(--accent-yellow)" stroke-width="1.3"/></svg>
        info@tulmexco.com
      </p>
      <p class="contact__row">
        <svg class="contact__icon" viewBox="0 0 12 12"><circle cx="6" cy="6" r="5" fill="none" stroke="var(--accent-yellow)" stroke-width="1.2"/><ellipse cx="6" cy="6" rx="2.2" ry="5" fill="none" stroke="var(--accent-yellow)" stroke-width="1"/><path d="M1 6 H11" stroke="var(--accent-yellow)" stroke-width="1"/></svg>
        www.tulmexco.com
      </p>
    </div>
  </section>

</div>
</body>
</html>
```